Label Design for Amber Kettle Specialty Coffee Roasters

We are a specialty coffee beans Roasting Shop named "Amber Kettle". We pack our beans in stand up poaches of varying sizes. We sell beans both to B2C and B2B and are looking to design stickers that will stand out. Our logo was designed with a black and white background. So far, we have been using white glossy bean bags and came up with a front label design that we would like to use for our labels.
We would like to see the design tweaked to fit both a white bag and a black one.
Currently, the attached front label design does not work on white bags. We would also like to have a back sticker designed that needs to include: 1- a description section for the type of beans used 2- a QR code section

Target Market(s)

Specialty beans in our area are typically liked by the younger generations 40 years and younger. Both male and females drink our coffee with varying income levels. But generally, middle class and above buy our coffee beans.

Requirements
Must have
• We are am looking for a sticker to be placed on a coffee bean bag. The sticker needs to contain the roasting shop's logo and brand name "Amber Kettle". Also, the sticker needs to have the following: country name, bean variety, weight (kg), roast date. The sticker needs to have the following specifications on a 5 point Likert scale (Strength, Fruitiness, Earthiness, Brightness). I uploaded a front label design that needs to be tweaked to fit both a white bag and a black one. The current design has owls representing the 5 point Likert scale and part of the shop's logo. We would like to keep that part of the design if possible. Currently, the attached front label design does not work on white bags.
We would also like to have a back sticker designed that needs to include: 1- a description section for the type of beans used 2- a QR code section
Nice to have
• The font that is used in the logo is League Gothic. It is okay to use this font or any other font if you find it more appropriate for the design.

```html
<!DOCTYPE html>
<html lang="en">
<head>
<meta charset="utf-8">
<title>Amber Kettle – Front Label</title>
<link href="https://fonts.googleapis.com/css2?family=League+Gothic&display=swap" rel="stylesheet">
<style>
  :root {
    --canvas: #e8e6e2;
    --label: #f3f3f3;
    --ink: #111111;
    --amber: #d9a760;
  }
  html, body {
    margin: 0;
    padding: 0;
    width: 1200px;
    height: 849px;
    overflow: hidden;
    background: var(--canvas);
  }
  .canvas {
    position: relative;
    width: 1200px;
    height: 849px;
  }
  .front-label {
    position: absolute;
    left: 220px;
    top: 45px;
    width: 760px;
    height: 759px;
    display: block;
  }
  .label-text {
    font-family: "League Gothic", "Oswald", sans-serif;
    fill: var(--ink);
  }
  .brand-name { font-size: 70px; letter-spacing: 1px; }
  .origin { font-size: 66px; letter-spacing: 1px; }
  .variety { font-size: 32px; letter-spacing: 3px; }
  .attribute { font-size: 30px; letter-spacing: 0.5px; }
  .meta-label { font-size: 28px; letter-spacing: 1px; }
  .meta-value { font-size: 40px; letter-spacing: 1px; }
  .rule { stroke: var(--ink); stroke-width: 3; }
  .frame { fill: none; stroke: var(--ink); stroke-width: 3; }
  .dot-on { fill: var(--ink); }
  .dot-off { fill: none; stroke: var(--ink); stroke-width: 2; }
</style>
</head>
<body>
<main class="canvas">
  <svg class="front-label" viewBox="0 0 878 877" xmlns="http://www.w3.org/2000/svg" aria-label="Amber Kettle front label, Colombia">
    <!-- label base -->
    <rect x="0" y="0" width="878" height="877" fill="var(--label)"/>
    <!-- amber band -->
    <rect x="0" y="602" width="878" height="275" fill="var(--amber)"/>
    <rect x="92" y="590" width="695" height="222" fill="var(--label)"/>
    <!-- outer frame -->
    <rect class="frame" x="28" y="27" width="823" height="823"/>

    <!-- brand -->
    <g class="brand">
      <circle cx="262" cy="226" r="20" fill="var(--ink)"/>
      <text class="label-text brand-name" x="298" y="252">AMBER KETTLE</text>
    </g>

    <!-- info box -->
    <rect class="frame" x="113" y="396" width="652" height="395" fill="var(--label)"/>
    <text class="label-text origin" x="439" y="466" text-anchor="middle">COLOMBIA</text>
    <line class="rule" x1="150" y1="487" x2="728" y2="487"/>
    <text class="label-text variety" x="439" y="530" text-anchor="middle">BEAN VARIETY</text>
    <line class="rule" x1="150" y1="549" x2="728" y2="549"/>

    <!-- tasting profile -->
    <g class="profile">
      <text class="label-text attribute" x="149" y="587">STRENGTH</text>
      <circle class="dot-on" cx="319" cy="575" r="11"/>
      <circle class="dot-on" cx="357" cy="575" r="11"/>
      <circle class="dot-off" cx="395" cy="575" r="11"/>
      <circle class="dot-off" cx="433" cy="575" r="11"/>
      <circle class="dot-off" cx="471" cy="575" r="11"/>
      <line class="rule" x1="150" y1="599" x2="547" y2="599"/>

      <text class="label-text attribute" x="149" y="636">FRUITINESS</text>
      <circle class="dot-on" cx="319" cy="624" r="11"/>
      <circle class="dot-off" cx="357" cy="624" r="11"/>
      <circle class="dot-off" cx="395" cy="624" r="11"/>
      <circle class="dot-off" cx="433" cy="624" r="11"/>
      <circle class="dot-off" cx="471" cy="624" r="11"/>
      <line class="rule" x1="150" y1="648" x2="728" y2="648"/>

      <text class="label-text attribute" x="149" y="685">EARTHINESS</text>
      <circle class="dot-on" cx="319" cy="673" r="11"/>
      <circle class="dot-on" cx="357" cy="673" r="11"/>
      <circle class="dot-on" cx="395" cy="673" r="11"/>
      <circle class="dot-off" cx="433" cy="673" r="11"/>
      <circle class="dot-off" cx="471" cy="673" r="11"/>
      <line class="rule" x1="150" y1="697" x2="547" y2="697"/>

      <text class="label-text attribute" x="149" y="735">BRIGHTNESS</text>
      <circle class="dot-on" cx="319" cy="723" r="11"/>
      <circle class="dot-on" cx="357" cy="723" r="11"/>
      <circle class="dot-on" cx="395" cy="723" r="11"/>
      <circle class="dot-on" cx="433" cy="723" r="11"/>
      <circle class="dot-off" cx="471" cy="723" r="11"/>
      <line class="rule" x1="150" y1="747" x2="728" y2="747"/>
    </g>

    <!-- roast details -->
    <line class="rule" x1="547" y1="551" x2="547" y2="747"/>
    <g class="details">
      <text class="label-text meta-label" x="640" y="586" text-anchor="middle">ROAST DATE:</text>
      <text class="label-text meta-value" x="640" y="632" text-anchor="middle">20/2/2020</text>
      <text class="label-text meta-label" x="640" y="685" text-anchor="middle">NET WEIGHT:</text>
      <text class="label-text meta-value" x="640" y="728" text-anchor="middle">60KG</text>
    </g>
  </svg>
</main>
</body>
</html>
```